Mine Engineering Consultancy specializing in
* Pit optimization
* Mine Design
* Scheduling
* Mine Rehabilitation

Mining

RVT Mining Pty Ltd
Dennis Holloway
Director/Principle Mining Engineer
Mobile 0418263591
Email dennis.holloway@rvtmining-example.com

```html
<!DOCTYPE html>
<html lang="en">
<head>
<meta charset="utf-8">
<title>RVT Mining Pty Ltd — Business Card</title>
<link rel="stylesheet" href="https://fonts.googleapis.com/css2?family=PT+Sans:wght@400;700&family=PT+Sans+Narrow:wght@400;700&display=swap">
<style>
  :root {
    --page-bg: #e4e2df;
    --card-top: #f7f8f9;
    --card-bottom: #eceef0;
    --brand-blue: #1f4f8f;
    --ink-dark: #2b2b2b;
    --ink-mid: #454545;
    --rule: #8a8a8a;
    --band-blue: #1d4f96;
    --band-dark: #1c1c1e;
  }
  * { margin: 0; padding: 0; box-sizing: border-box; }
  html, body {
    width: 1200px; height: 969px; overflow: hidden;
    background: var(--page-bg);
  }
  .canvas { position: relative; width: 1200px; height: 969px; }
  .card {
    position: absolute; left: 70px; top: 183px;
    width: 1060px; height: 602px; overflow: hidden;
    background: linear-gradient(160deg, var(--card-top), var(--card-bottom));
    font-family: "PT Sans", Arial, sans-serif;
    box-shadow: 0 6px 24px rgba(0,0,0,0.12);
  }
  .company-name {
    position: absolute; right: 53px; top: 120px;
    font-size: 44px; font-weight: 400; color: var(--brand-blue);
    white-space: nowrap;
  }
  .name-marker {
    position: absolute; left: 0; top: 303px;
    width: 15px; height: 73px; background: var(--brand-blue);
  }
  .person-name {
    position: absolute; left: 58px; top: 300px;
    font-size: 34px; font-weight: 700; color: var(--brand-blue);
  }
  .person-title {
    position: absolute; left: 58px; top: 345px;
    font-size: 25px; color: var(--ink-dark);
  }
  .divider {
    position: absolute; left: 58px; top: 397px;
    width: 946px; height: 1px; background: var(--rule);
  }
  .contact-list { position: absolute; left: 62px; top: 424px; list-style: none; }
  .contact-item {
    display: flex; align-items: center; height: 41px;
    font-size: 22px; color: var(--ink-mid);
  }
  .contact-item svg { width: 24px; height: 24px; margin-right: 16px; fill: var(--ink-mid); }
  .services {
    position: absolute; right: 53px; top: 424px; text-align: right;
  }
  .services-heading {
    font-family: "PT Sans Narrow", Arial, sans-serif;
    font-size: 25px; font-weight: 700; color: var(--brand-blue); height: 41px;
  }
  .services-row { font-size: 22px; color: var(--ink-dark); height: 40px; }
  .services-row .dot { margin: 0 10px; }
  .footer-band { position: absolute; left: 0; bottom: 0; width: 1060px; height: 27px; }
</style>
</head>
<body>
<div class="canvas">
  <div class="card">
    <div class="company-name">RVT Mining Pty Ltd</div>

    <div class="name-marker"></div>
    <div class="person-name">Dennis Holloway</div>
    <div class="person-title">Director/Principle Mining Engineer</div>
    <div class="divider"></div>

    <ul class="contact-list">
      <li class="contact-item">
        <svg viewBox="0 0 24 24" aria-hidden="true"><path d="M6.6 10.8a15.1 15.1 0 0 0 6.6 6.6l2.2-2.2a1 1 0 0 1 1-.25 11.4 11.4 0 0 0 3.6.57 1 1 0 0 1 1 1V20a1 1 0 0 1-1 1A17 17 0 0 1 3 4a1 1 0 0 1 1-1h3.5a1 1 0 0 1 1 1c0 1.25.2 2.45.57 3.57a1 1 0 0 1-.25 1z"/></svg>
        0418263591
      </li>
      <li class="contact-item">
        <svg viewBox="0 0 24 24" aria-hidden="true"><circle cx="12" cy="12" r="10"/><path d="M5 9h5l2 3-3 3 1 4M14 4l-1 4 4 2 3-1M15 14l3 2-1 3" stroke="#f2f3f4" stroke-width="1.6" fill="none"/></svg>
        www.rvtmining-example.com
      </li>
      <li class="contact-item">
        <svg viewBox="0 0 24 24" aria-hidden="true"><path d="M2 5h20v14H2z"/><path d="M2 5l10 8 10-8" stroke="#f2f3f4" stroke-width="1.6" fill="none"/></svg>
        dennis.holloway@rvtmining-example.com
      </li>
    </ul>

    <div class="services">
      <div class="services-heading">Mine Engineering Consultancy specializing in</div>
      <div class="services-row">Pit optimization<span class="dot">•</span>Mine Design</div>
      <div class="services-row">Scheduling<span class="dot">•</span>Mine Rehabilitation</div>
    </div>

    <svg class="footer-band" viewBox="0 0 1060 27" preserveAspectRatio="none" aria-hidden="true">
      <polygon points="0,0 700,0 690,27 0,27" fill="var(--band-blue)"/>
      <polygon points="707,0 1060,0 1060,27 697,27" fill="var(--band-dark)"/>
    </svg>
  </div>
</div>
</body>
</html>
```